Gordon the Glazier
stationary
Gordon the Glazier -
Creative Brief
Simple
Desmond Pryce
PO Box 417 KELDARRA VIC 3062
gordon@gordontheglazier.com.au
www.gordontheglazier.com.au
I don't need my name or address on the business card -- it just needs to be a general "Gordon the Glazier" card with phone and email contact and web address. Could you also put "Member of the TGWB" somewhere -- this text doesn't have to be bold/eye-catching. It would be good if you could design a business card, letterhead and envelope design

```html
<!DOCTYPE html>
<html lang="en">
<head>
<meta charset="utf-8">
<title>Gordon the Glazier – Business Card</title>
<link rel="stylesheet" href="https://fonts.googleapis.com/css2?family=Montserrat:wght@500;700&family=Cormorant+Garamond:wght@500&display=swap">
<style>
  :root {
    --page-bg: #f2f2f3;
    --label-grey: #6d6d72;
    --card-white: #ffffff;
    --brand-navy: #2d3e9a;
    --brand-cyan: #2aa6dc;
    --text-grey: #5c6070;
    --back-navy-light: #3f52b0;
    --back-navy-dark: #27337f;
    --back-cyan-light: #4fc6ea;
    --back-cyan-dark: #1f9fd2;
    --card-shadow: 0 10px 14px rgba(0, 0, 0, 0.28);
  }
  * { box-sizing: border-box; margin: 0; padding: 0; }
  html, body { width: 1200px; height: 379px; overflow: hidden; }
  body {
    background: var(--page-bg);
    font-family: "Montserrat", Arial, sans-serif;
    position: relative;
  }
  .view-label {
    position: absolute;
    top: 12px;
    width: 200px;
    text-align: center;
    font-family: "Cormorant Garamond", Georgia, serif;
    font-weight: 500;
    font-size: 24px;
    letter-spacing: 2px;
    color: var(--label-grey);
  }
  .card {
    position: absolute;
    top: 101px;
    height: 206px;
    box-shadow: var(--card-shadow);
    overflow: hidden;
  }
  .card-front { left: 53px; width: 355px; background: var(--card-white); }
  .card-back-navy {
    left: 439px; width: 324px;
    background: radial-gradient(circle at 50% 45%, var(--back-navy-light), var(--back-navy-dark) 80%);
  }
  .card-back-cyan {
    left: 802px; width: 326px;
    background: radial-gradient(circle at 50% 45%, var(--back-cyan-light), var(--back-cyan-dark) 85%);
  }
  .brand {
    position: absolute;
    left: 22px; top: 30px;
    display: flex; align-items: center; gap: 8px;
  }
  .brand-square {
    width: 30px; height: 30px;
    background: var(--brand-navy);
    border-radius: 4px;
  }
  .brand-name {
    font-weight: 700;
    font-size: 22px;
    line-height: 1;
    color: var(--brand-navy);
    width: 140px;
  }
  .contact {
    position: absolute;
    left: 22px; bottom: 26px;
    font-size: 7.5px;
    line-height: 1.55;
    color: var(--brand-cyan);
    font-weight: 500;
  }
  .membership {
    position: absolute;
    right: 48px; bottom: 52px;
    font-size: 7.5px;
    color: var(--text-grey);
    font-weight: 500;
  }
  .edge-tab {
    position: absolute;
    left: 0; bottom: 14px;
    width: 7px; height: 26px;
    background: var(--brand-navy);
  }
  .back-brand {
    position: absolute;
    left: 0; right: 0; top: 84px;
    text-align: center;
    font-weight: 700;
    font-size: 14px;
    color: var(--card-white);
  }
</style>
</head>
<body>
  <div class="view-label" style="left:130px">FRONT</div>
  <div class="view-label" style="left:501px">BACK</div>
  <div class="view-label" style="left:865px">BACK</div>

  <section class="card card-front">
    <div class="brand">
      <span class="brand-square"></span>
      <span class="brand-name">Gordon the Glazier</span>
    </div>
    <div class="contact">
      <p>P: 0400 512 384</p>
      <p>E: pjholloway@gordontheglazier.com.au</p>
      <p>www.gordontheglazier.com.au</p>
    </div>
    <p class="membership">Member of the TGWB</p>
    <span class="edge-tab"></span>
  </section>

  <section class="card card-back-navy">
    <p class="back-brand">Gordon the Glazier</p>
  </section>

  <section class="card card-back-cyan">
    <p class="back-brand">Gordon the Glazier</p>
  </section>
</body>
</html>
```